Peach Point of Sale Cards for Grocery Retail Markets

We are looking to update our peach point of sale card and price card. The cards will need to be 7" x 11" with a .125 bleed - one sided. See attached for the old versions. We would like this to use photos that look like true Cascadia State Peaches. Here are the bullet points we would like to use: - New Crop!- Tree Ripened- Excellent FlavorNOTE: The price card just needs to have a space where a retailer can write in the sale price of the item. See attachment with the white box.

Target Market(s)

Retail market shoppers

Requirements
Must have
• Pictures of Peaches Only

```html
<!DOCTYPE html>
<html lang="en">
<head>
<meta charset="utf-8">
<title>Peach Point of Sale and Price Cards</title>
<link rel="stylesheet" href="https://fonts.googleapis.com/css2?family=League+Spartan:wght@700&family=Quicksand:wght@300;400&family=Sacramento&display=swap">
<style>
  :root {
    --page-bg: #ebe7e2;
    --card-white: #ffffff;
    --band-mint: #c8f5cc;
    --heading-green: #136b1a;
    --script-red: #a3161b;
    --bullet-coral: #e8343a;
    --tick-green: #2a9a2f;
    --badge-green: #33c23f;
    --peach-warm: #f08a4e;
    --peach-soft: #f6c2a4;
  }
  * { box-sizing: border-box; margin: 0; padding: 0; }
  html, body {
    width: 1200px; height: 952px; overflow: hidden;
    background: var(--page-bg);
  }
  .sheet { position: relative; width: 1200px; height: 952px; }

  .card {
    position: absolute; width: 699px; height: 437px;
    background: var(--card-white); overflow: hidden;
    box-shadow: 0 2px 8px rgba(0,0,0,.12);
  }
  .card--display { left: 30px; top: 32px; }
  .card--price { left: 470px; top: 490px; }

  .peach-photo {
    position: absolute; left: 0; top: 0; width: 100%; height: 100%;
    background:
      radial-gradient(ellipse 32% 40% at 36% 74%, var(--peach-warm) 0%, rgba(240,120,70,.85) 45%, rgba(240,120,70,0) 100%),
      radial-gradient(ellipse 18% 30% at 10% 68%, rgba(242,150,70,.9) 0%, rgba(242,150,70,0) 100%),
      radial-gradient(ellipse 22% 28% at 50% 55%, rgba(246,178,160,.7) 0%, rgba(246,178,160,0) 100%),
      linear-gradient(180deg, rgba(255,255,255,0) 55%, rgba(160,100,70,.35) 85%),
      linear-gradient(90deg, var(--peach-soft) 0%, rgba(250,215,200,.6) 45%, rgba(255,255,255,0) 80%);
  }
  .card--price .peach-photo { top: 80px; height: calc(100% - 80px); }

  .title-band {
    position: absolute; left: 0; width: 100%; height: 42px;
    background: var(--band-mint);
    display: flex; align-items: center; justify-content: center;
  }
  .card--display .title-band { top: 1px; }
  .card--price .title-band { top: 43px; height: 37px; }
  .title-band h1 {
    font-family: "League Spartan", sans-serif; font-weight: 700;
    font-size: 33px; letter-spacing: 5px; color: var(--heading-green);
    padding-top: 6px; white-space: nowrap;
  }

  .tagline {
    position: absolute; left: 140px; right: 10px; white-space: nowrap;
    font-family: "Sacramento", cursive; font-weight: 400;
    font-size: 58px; letter-spacing: 7px; color: var(--script-red);
    line-height: 1;
  }
  .card--display .tagline { top: 50px; }
  .card--price .tagline { top: 88px; }

  .benefits { position: absolute; left: 368px; list-style: none; }
  .card--display .benefits { top: 136px; }
  .card--price .benefits { top: 160px; }
  .benefits li {
    display: flex; align-items: center; height: 47px;
    font-family: "Quicksand", sans-serif; font-weight: 300;
    font-size: 27px; letter-spacing: 4px; color: var(--bullet-coral);
    white-space: nowrap;
  }
  .benefits svg { width: 14px; height: 12px; margin-right: 7px; flex: none; }

  .quality-seal {
    position: absolute; left: 60px; top: 276px; width: 134px; height: 120px;
    border: 3px solid var(--badge-green); border-radius: 50%;
    transform: rotate(-12deg);
  }

  .swoosh { position: absolute; left: 0; top: 0; width: 699px; height: 437px; }

  .grower-mark {
    position: absolute; left: 546px; top: 304px; width: 88px; height: 88px;
    border-radius: 50%; background: var(--peach-warm);
  }
  .grower-name {
    position: absolute; left: 535px; top: 355px; width: 110px; text-align: center;
    font-family: "League Spartan", sans-serif; font-weight: 700;
    font-size: 13px; letter-spacing: 1px; color: var(--card-white);
  }

  .sponsor {
    position: absolute; right: 22px; bottom: 6px;
    font-family: "Sacramento", cursive; font-size: 24px;
    letter-spacing: 3px; color: var(--card-white); white-space: nowrap;
  }

  .price-tag { position: absolute; left: 9px; top: 166px; width: 150px; height: 100px; }
</style>
</head>
<body>
<main class="sheet">

  <section class="card card--display" aria-label="Peach point of sale card">
    <div class="peach-photo" role="img" aria-label="Photo of ripe peaches on a wooden table with a basket behind"></div>
    <svg class="swoosh" viewBox="0 0 699 437" aria-hidden="true">
      <defs>
        <linearGradient id="redA" x1="0" x2="1"><stop offset="0" stop-color="#7d0808"/><stop offset=".6" stop-color="#c80d0d"/><stop offset="1" stop-color="#d81010"/></linearGradient>
        <linearGradient id="orangeA" x1="0" x2="1"><stop offset="0" stop-color="#e88a2a"/><stop offset="1" stop-color="#f8d2a6"/></linearGradient>
      </defs>
      <path d="M0 386 C190 410 430 360 699 308 L699 437 L0 437 Z" fill="url(#orangeA)"/>
      <path d="M0 400 C210 430 450 380 699 340 L699 437 L0 437 Z" fill="url(#redA)"/>
    </svg>
    <header class="title-band"><h1>CASCADIA STATE PEACHES</h1></header>
    <p class="tagline">Taste the Difference!</p>
    <ul class="benefits">
      <li><svg viewBox="0 0 14 12"><path d="M1 6.5 L5 10 L13 2" fill="none" stroke="#2a9a2f" stroke-width="2.6"/></svg>New Crop!</li>
      <li><svg viewBox="0 0 14 12"><path d="M1 6.5 L5 10 L13 2" fill="none" stroke="#2a9a2f" stroke-width="2.6"/></svg>Tree Ripened</li>
      <li><svg viewBox="0 0 14 12"><path d="M1 6.5 L5 10 L13 2" fill="none" stroke="#2a9a2f" stroke-width="2.6"/></svg>Excellent Flavor</li>
    </ul>
    <div class="quality-seal" aria-hidden="true"></div>
    <div class="grower-mark" aria-hidden="true"></div>
    <p class="grower-name">cascadia</p>
    <p class="sponsor">Cascade Orchard Growers Council</p>
  </section>

  <section class="card card--price" aria-label="Peach price card">
    <div class="peach-photo" role="img" aria-label="Photo of ripe peaches on a wooden table with a basket behind"></div>
    <svg class="swoosh" viewBox="0 0 699 437" aria-hidden="true">
      <defs>
        <linearGradient id="redB" x1="0" x2="1"><stop offset="0" stop-color="#7d0808"/><stop offset=".6" stop-color="#c80d0d"/><stop offset="1" stop-color="#d81010"/></linearGradient>
        <linearGradient id="orangeB" x1="0" x2="1"><stop offset="0" stop-color="#e88a2a"/><stop offset="1" stop-color="#f8d2a6"/></linearGradient>
      </defs>
      <path d="M0 386 C190 410 430 360 699 308 L699 437 L0 437 Z" fill="url(#orangeB)"/>
      <path d="M0 400 C210 430 450 380 699 340 L699 437 L0 437 Z" fill="url(#redB)"/>
    </svg>
    <header class="title-band"><h1>CASCADIA STATE PEACHES</h1></header>
    <p class="tagline">Taste the Difference!</p>
    <ul class="benefits">
      <li><svg viewBox="0 0 14 12"><path d="M1 6.5 L5 10 L13 2" fill="none" stroke="#2a9a2f" stroke-width="2.6"/></svg>New Crop!</li>
      <li><svg viewBox="0 0 14 12"><path d="M1 6.5 L5 10 L13 2" fill="none" stroke="#2a9a2f" stroke-width="2.6"/></svg>Tree Ripened</li>
      <li><svg viewBox="0 0 14 12"><path d="M1 6.5 L5 10 L13 2" fill="none" stroke="#2a9a2f" stroke-width="2.6"/></svg>Excellent Flavor</li>
    </ul>
    <div class="quality-seal" aria-hidden="true"></div>
    <svg class="price-tag" viewBox="0 0 150 100" aria-label="Space to write the sale price">
      <path d="M2 6 Q2 2 6 2 L124 2 L148 26 L148 74 L124 98 L6 98 Q2 98 2 94 Z" fill="#c41717"/>
      <rect x="7" y="6" width="99" height="88" rx="5" fill="#ffffff"/>
      <circle cx="124" cy="50" r="11" fill="#e8e0dc"/>
      <circle cx="124" cy="50" r="6" fill="#e89a5a"/>
      <path d="M131 46 Q150 30 170 44" fill="none" stroke="#e8e0dc" stroke-width="1.2"/>
    </svg>
    <div class="grower-mark" aria-hidden="true"></div>
    <p class="grower-name">cascadia</p>
    <p class="sponsor">Cascade Orchard Growers Council</p>
  </section>

</main>
</body>
</html>
```